Lumorax Helpdesk overview brochure

Take the word document that is attached and turn it into a brochure. (Thinking one page, front and back.) the only existing branding/colors we have is the logo that is on the document. It may require a phone all or a bit of back and forth in text to explain some of the concepts in the attached document.

Target Market(s)

Call centers

Industry/Entity Type

It Service

Font styles to use
Sans Serif

Colors

Designer to choose colors to be used in the design.

Requirements
Must have
• A crisp professional look

```html
<!DOCTYPE html>
<html lang="en">
<head>
<meta charset="utf-8">
<title>Lumorax Helpdesk overview brochure</title>
<link href="https://fonts.googleapis.com/css2?family=Oswald:wght@500;600&family=Source+Sans+3:wght@400;600;700&display=swap" rel="stylesheet">
<style>
:root{
  --bg:#2e2e30;
  --paper:#ffffff;
  --blue:#1a9ad6;
  --panel:#2a7fc6;
  --panel-deep:#2578bd;
  --slate:#5a5b5e;
  --tab:#4a4b4e;
  --ink:#4d4d4f;
  --text:#333336;
  --frame:#dcdcdc;
}
*{box-sizing:border-box;margin:0;padding:0}
html,body{width:1200px;height:796px;overflow:hidden;background:var(--bg)}
body{font-family:"Source Sans 3",sans-serif;color:var(--text);position:relative}
.page{position:absolute;top:56px;width:530px;height:684px;background:var(--paper);overflow:hidden}
.page--front{left:58px}
.page--back{left:614px}
.abs{position:absolute}

/* front */
.headline{left:20px;width:490px;top:30px;text-align:center;color:var(--blue);font-weight:700;font-size:22.5px;line-height:26.5px}
.brand{display:flex;align-items:center;gap:10px}
.brand__mark{width:46px;height:46px;border-radius:50%;background:var(--blue);flex:none}
.brand__name{font-size:27px;font-weight:600;color:var(--blue);letter-spacing:.5px;line-height:1}
.front-brand{left:140px;top:145px}
.body-col{font-size:8.2px;line-height:11.3px;color:#444;text-align:justify}
.body-col p+p{margin-top:11px}
.col-a{left:26px;top:224px;width:224px}
.col-b{left:284px;top:224px;width:218px;text-align:left}
.col-rule{left:266px;top:228px;width:1px;height:120px;background:#ddd}
.section-title{left:26px;top:362px;font-family:"Oswald",sans-serif;font-weight:500;font-size:20px;color:var(--slate)}
.cost-panel{left:0;top:428px;width:530px;height:256px;background:var(--panel)}
.call-tab{left:14px;top:400px;width:306px;height:38px}
.call-tab span{position:absolute;left:48px;top:6px;font-family:"Oswald",sans-serif;font-weight:500;font-size:20px;color:#fff;letter-spacing:.3px}
.channel{left:26px;display:flex;align-items:center;gap:11px}
.channel__icon{width:64px;height:42px;background:#f2f4f6;display:flex;align-items:center;justify-content:center}
.channel__text{color:#fff;font-weight:700;font-size:13px;line-height:17px}
.photo{background:linear-gradient(160deg,#cfd5da,#8d9aa6 55%,#3f4954)}
.front-photo{left:336px;top:461px;width:162px;height:197px}
.footnote{left:26px;top:648px;color:#e6f0fa;font-size:10.5px}

/* back */
.channel-row{left:26px;top:40px;width:478px;display:flex;justify-content:space-between}
.chip{display:flex;align-items:center;gap:4px;font-size:11px;font-weight:700;color:var(--ink)}
.chip__dot{width:14px;height:14px;border-radius:3px;background:var(--blue)}
.tagline{left:0;width:530px;top:104px;text-align:center;font-size:14.5px;line-height:19px;color:#222}
.engage{left:30px;top:160px;width:470px;height:381px;background:var(--frame)}
.engage__head{height:27px;background:var(--tab);color:#fff;text-align:center;font-family:"Oswald",sans-serif;font-weight:500;font-size:17px;line-height:27px}
.engage__body{position:absolute;left:8px;top:27px;width:454px;height:346px;background:var(--panel-deep);color:#fff}
.engage h3{font-size:17px;font-weight:700}
.proposal{left:14px;top:10px}
.proposal p{font-size:12px;line-height:14px;margin-top:4px}
.proposal p small{display:block;font-size:9.5px}
.engage-rule{left:14px;right:14px;top:88px;height:1px;background:#7fb3e0}
.engage-divider{left:232px;top:102px;width:1px;height:224px;background:#6aa6d9}
.col-engage{left:14px;top:102px;width:212px}
.col-report{left:258px;top:102px;width:190px}
.col-engage .lead{font-size:11.3px;font-weight:700;line-height:12.5px;margin:8px 0 12px}
.bullets{list-style:none;font-size:9.2px;line-height:11.6px}
.bullets li{position:relative;padding-left:12px;margin-bottom:4px}
.bullets li::before{content:"";position:absolute;left:0;top:3px;width:5px;height:5px;border-radius:50%;border:1.5px solid #fff}
.col-report .bullets{margin-top:10px}
.back-brand{left:30px;top:566px}
.url{left:30px;top:630px;font-size:20.5px;font-weight:700;letter-spacing:1.4px;color:#2b2b2d}
.back-photo{left:366px;top:547px;width:134px;height:114px}
</style>
</head>
<body>

<section class="page page--front">
  <h1 class="abs headline">Lumorax Helpdesk helps contact centers serve new customer access channels, improve customer service, and lower costs of operation.</h1>

  <div class="abs brand front-brand">
    <span class="brand__mark"></span>
    <span class="brand__name">Lumorax Helpdesk</span>
  </div>

  <div class="abs body-col col-a">
    <p>The huge popularity of social media and messaging is creating customer preferences to communicate with your company using SMS text messaging, Chatterly Messenger, Teamloop, Vocalis, Orbi Voice, Hearth Hub, and many other new channels.</p>
    <p>App fatigue has set in. Customers are weary of installing, updating and learning how to use mobile apps. Your customers want to communicate with you using their messaging service of choice or just talk into their smart phone, computer, Orbi Voice or similar device.</p>
  </div>
  <div class="abs col-rule"></div>
  <div class="abs body-col col-b">
    <p>Sensible automation of customer interactions on these new channels can provide better service at even lower costs of operation.</p>
    <p>According to Northfield Research's report, by 2020, 85% of customer interactions will be managed without a human.</p>
    <p>Using specific techniques, Lumorax Helpdesk will help you shift some traffic from higher cost telephone calls to lower cost messaging channels. Shaping your traffic into lower cost channels has great financial benefits.</p>
  </div>

  <h2 class="abs section-title">Existing channels have different costs</h2>

  <div class="abs cost-panel"></div>
  <div class="abs call-tab">
    <svg width="306" height="38" viewBox="0 0 306 38"><path d="M0 38 L30 4 Q34 0 40 0 H266 Q272 0 276 4 L306 38 Z" fill="var(--tab)"/></svg>
    <span>Call Us: 555-014-2287</span>
  </div>

  <div class="abs channel" style="top:461px">
    <div class="channel__icon">
      <svg width="30" height="30" viewBox="0 0 24 24"><path d="M6.6 10.8a15 15 0 0 0 6.6 6.6l2.2-2.2a1 1 0 0 1 1-.25 11.4 11.4 0 0 0 3.6.57 1 1 0 0 1 1 1V20a1 1 0 0 1-1 1A17 17 0 0 1 3 4a1 1 0 0 1 1-1h3.5a1 1 0 0 1 1 1c0 1.25.2 2.45.57 3.57a1 1 0 0 1-.25 1z" fill="var(--panel)"/></svg>
    </div>
    <div class="channel__text">Telephone call with a live agent<br>Average cost per call is $17 *</div>
  </div>
  <div class="abs channel" style="top:519px">
    <div class="channel__icon">
      <svg width="32" height="24" viewBox="0 0 32 24"><rect x="1" y="1" width="30" height="22" rx="2" fill="var(--panel)"/><path d="M2 3 L16 14 L30 3" stroke="#fff" stroke-width="2" fill="none"/></svg>
    </div>
    <div class="channel__text">Email with a live agent<br>Average cost per email is $15*</div>
  </div>
  <div class="abs channel" style="top:576px">
    <div class="channel__icon">
      <svg width="34" height="30" viewBox="0 0 34 30"><path d="M4 2 H30 Q32 2 32 4 V20 Q32 22 30 22 H14 L7 28 V22 H4 Q2 22 2 20 V4 Q2 2 4 2Z" fill="var(--panel)"/></svg>
    </div>
    <div class="channel__text">Webchat with a live agent<br>Average cost per web chat is $12*</div>
  </div>

  <div class="abs photo front-photo" role="img" aria-label="Photo of a smiling contact center agent on a desk telephone"></div>
  <p class="abs footnote">*Above costs are sited from an CSRI research paper</p>
</section>

<section class="page page--back">
  <div class="abs channel-row">
    <span class="chip"><span class="chip__dot"></span>SMS</span>
    <span class="chip"><span class="chip__dot"></span>Teamloop</span>
    <span class="chip"><span class="chip__dot"></span>Orbi Voice</span>
    <span class="chip"><span class="chip__dot"></span>Zipchat</span>
    <span class="chip"><span class="chip__dot"></span>Hearth Hub</span>
    <span class="chip"><span class="chip__dot"></span>Wavetalk</span>
    <span class="chip"><span class="chip__dot"></span>Pingly</span>
  </div>

  <p class="abs tagline">With these new channels, the cost is similar to webchat.<br>Carefully automated interactions are at an even lower cost</p>

  <div class="abs engage">
    <div class="engage__head">Engagement model</div>
    <div class="engage__body">
      <div class="abs proposal">
        <h3>Proposal</h3>
        <p>Lumorax Helpdesk provides a written proposal.<small>The proposal will describe our engagement methodologies and costs.</small></p>
      </div>
      <div class="abs engage-rule"></div>
      <div class="abs engage-divider"></div>
      <div class="abs col-engage">
        <h3>Engagement</h3>
        <p class="lead">Lumorax Helpdesk will meet with all the relevant stake holders on site and gather information to identify:</p>
        <ul class="bullets">
          <li>Historical traffic patterns.</li>
          <li>Actual costs by channel</li>
          <li>Review marketing plans that may impact customer service</li>
          <li>Review product plans that may impact customer service.</li>
          <li>Explore competition landscape as it relates to customer service.</li>
          <li>Review the existing corporate data store, analytics and reporting</li>
          <li>Review the current plans, metrics and budgets for customer service support</li>
        </ul>
      </div>
      <div class="abs col-report">
        <h3>Transformation Report</h3>
        <ul class="bullets">
          <li>Executive summary</li>
          <li>Cost analysis per contact by channel</li>
          <li>Traffic patterns by channel</li>
          <li>Probable impacts of product and marketing plans</li>
          <li>Recommendations for achieving competitive advantage through service</li>
          <li>Recommendations for new channel types</li>
          <li>Recommendations for traffic shaping</li>
          <li>Near and long-term options for sensible automation</li>
          <li>Technology recommendations for implementing new channels</li>
          <li>Projected financial impact of recommendations</li>
        </ul>
      </div>
    </div>
  </div>

  <div class="abs brand back-brand">
    <span class="brand__mark"></span>
    <span class="brand__name">Lumorax Helpdesk</span>
  </div>
  <p class="abs url">www.LumoraxSolutions.net</p>
  <div class="abs photo back-photo" role="img" aria-label="Photo of a support agent wearing a headset with colleagues behind"></div>
</section>

</body>
</html>
```